Brochure Design Project

We are a payroll company. We offer a wide variety of products and services:
1. Payroll Processing
2. Employee Direct Deposit
3. Time and attendance
4. HR services
5. Employee Employee Benefits

I'd like to develop a one page template that uses a combination of our logo (attached), colors (attached) and possible a picture. The picture could be shown as an option as it may change based on the product or service.

Target Market(s)

Adults in the United States ages 22-50. Typically these people are accountants, human resource professionals or entrepreneurs. The payroll industry is dominated by 3 large payroll processors, QLM, Wendrafy and Tolvarex. These companies are very impersonal and make it difficult to resolve issues when they arise. We have grown to over 400 clients by being the opposite of the big guys,

Industry/Entity Type

It Company

Font styles to use
Sans Serif

Requirements
Must have
• The brochure can be one or two pages.
Nice to have
• I'll know it when I see it but I can't describe it. I have attached a few brochures that have caught my eye.
Should not have
• No cartoons. No money signs. Hip, new, fresh are words I'd use to describe the winning product. Of the three people I described in my target market, the entrepreneur is the market I'd most like to target.

```html
<!DOCTYPE html>
<html lang="en">
<head>
<meta charset="utf-8">
<title>Tallyway Payroll Brochure</title>
<link href="https://fonts.googleapis.com/css2?family=Arimo:wght@400;700&display=swap" rel="stylesheet">
<style>
  :root{
    --navy:#1c2a6e;
    --blue:#1f44b0;
    --green:#8cc43f;
    --green-light:#b5dc74;
    --grey-text:#4a4a4a;
    --paper:#ffffff;
  }
  *{margin:0;padding:0;box-sizing:border-box}
  html,body{width:831px;height:1200px;overflow:hidden;background:var(--paper)}
  body{font-family:"Arimo",Arial,sans-serif;position:relative}
  .brochure{position:relative;width:831px;height:1200px;overflow:hidden;background:var(--paper)}
  .top-rule{position:absolute;left:0;top:36px;width:831px;height:8px;background:var(--navy)}
  .top-rule-accent{position:absolute;left:0;top:44px;width:500px;height:6px;background:var(--green-light)}
  .header-band{position:absolute;left:0;top:60px;width:500px;height:92px;background:var(--green);display:flex;align-items:center;padding-left:36px}
  .header-title{font-size:40px;font-weight:400;color:var(--navy);letter-spacing:0.5px}
  .brand{position:absolute;right:24px;top:88px;display:flex;align-items:center;gap:10px}
  .brand-mark{width:26px;height:26px;border-radius:50%;background:var(--green)}
  .brand-name{font-size:28px;font-weight:700;color:var(--navy);white-space:nowrap}
  .hero-shapes{position:absolute;left:0;top:150px;width:340px;height:400px}
  .intro-heading{position:absolute;left:300px;top:196px;font-size:28px;font-weight:400;color:var(--navy)}
  .intro-lead{position:absolute;left:300px;top:232px;width:505px;font-size:18px;line-height:1.25;color:var(--blue)}
  .intro-body{position:absolute;left:330px;top:360px;width:470px;font-size:16.5px;line-height:1.3;color:var(--grey-text);text-align:center}
  .column-left{position:absolute;left:26px;top:545px;width:362px;font-size:16.5px;line-height:1.3;color:var(--grey-text);text-align:center}
  .column-right{position:absolute;left:415px;top:535px;width:392px;height:585px;background:var(--navy);padding:16px 22px;color:#fff;font-size:16.5px;line-height:1.3;text-align:center}
  .footer-band{position:absolute;left:0;top:1150px;width:831px;height:50px;background:var(--navy)}
  .footer-accent{position:absolute;left:0;top:1150px;width:300px;height:10px;background:var(--green)}
</style>
</head>
<body>
<div class="brochure">
  <div class="top-rule"></div>
  <div class="top-rule-accent"></div>
  <div class="header-band"><h1 class="header-title">YOUR TEXT HERE</h1></div>
  <div class="brand"><span class="brand-mark"></span><span class="brand-name">Tallyway Payroll</span></div>

  <svg class="hero-shapes" viewBox="0 0 340 400" xmlns="http://www.w3.org/2000/svg">
    <defs>
      <linearGradient id="officeTone" x1="0" y1="0" x2="1" y2="1">
        <stop offset="0" stop-color="#cfe0ea"/>
        <stop offset="0.5" stop-color="#6d90b8"/>
        <stop offset="1" stop-color="#2c4f8c"/>
      </linearGradient>
    </defs>
    <polygon points="0,0 230,0 292,205 230,390 0,390" fill="#1c2a6e"/>
    <polygon points="0,60 200,60 270,200 0,200" fill="#8cc43f"/>
    <polygon points="18,95 220,95 268,205 220,320 18,320" fill="url(#officeTone)" role="img" aria-label="Photo of a bright modern office with desks and chairs"/>
    <polygon points="0,300 150,390 0,390" fill="#8cc43f"/>
  </svg>

  <h2 class="intro-heading">LOREM ISPUM</h2>
  <p class="intro-lead">Lorem ipsum dolor sit amet, temporibus liberavisse sed cu, an aliquip equidem principes usu. Ex quas suavitate accusamus pri, natum posse perfecto pri te. Ei eam soluta consectetuer, sumo ferri cum ex.</p>
  <p class="intro-body">Lorem ipsum dolor sit amet, temporibus liberavisse sed cu, an aliquip equidem principes usu. Ex quas suavitate accusamus pri, natum posse perfecto pri te. Ei eam soluta consectetuer, sumo ferri cum ex. At sed modo numquam epicurei. Ad nemore inure condusionemque est. An eos affert dolorum veritus. Sit ad forensibus moderatius, eum an iudicabit liberavisse, per mundi.</p>

  <p class="column-left">Lorem ipsum dolor sit amet, temporibus liberavisse sed cu, an aliquip equidem principes usu. Ex quas suavitate accusamus pri, natum posse perfecto pri te. Ei eam soluta consectetuer, sumo ferri cum ex. At sed modo numquam epicurei. Ad nemore inure condusionemque est. An eos affert dolorum veritus. Sit ad forensibus moderatius, eum an iudicabit liberavisse, per mundi. Lorem ipsum dolor sit amet, temporibus liberavisse sed cu, an aliquip equidem principes usu. Ex quas suavitate accusamus pri, natum posse perfecto pri te. Ei eam soluta consectetuer, sumo ferri cum ex. At sed modo numquam epicurei. Ad nemore inure condusionemque est. An eos affert dolorum veritus. Sit ad forensibus moderatius, eum an iudicabit liberavisse, per mundi. At sed modo numquam epicurei. Ad nemore inure condusionemque est. An eos affert dolorum veritus. Sit ad forensibus moderatius, eum an iudicabit liberavisse, per mundi.</p>

  <div class="column-right"><p>Lorem ipsum dolor sit amet, temporibus liberavisse sed cu, an aliquip equidem principes usu. Ex quas suavitate accusamus pri, natum posse perfecto pri te. Ei eam soluta consectetuer, sumo ferri cum ex. At sed modo numquam epicurei. Ad nemore inure condusionemque est. An eos affert dolorum veritus. Sit ad forensibus moderatius, eum an iudicabit liberavisse, per mundi. Lorem ipsum dolor sit amet, temporibus liberavisse sed cu, an aliquip equidem principes usu. Ex quas suavitate accusamus pri, natum posse perfecto pri te. Ei eam soluta consectetuer, sumo ferri cum ex. At sed modo numquam epicurei. Ad nemore inure condusionemque est. An eos affert dolorum veritus. Sit ad forensibus moderatius, eum an iudicabit liberavisse, per mundi. At sed modo numquam epicurei. Ad nemore inure condusionemque est. An eos affert dolorum veritus. Sit ad forensibus moderatius, eum an iudicabit liberavisse, per mundi.</p></div>

  <div class="footer-band"></div>
  <div class="footer-accent"></div>
</div>
</body>
</html>
```